new ownership of a business

Tax & accounting firm including payroll processing, business consulting, bookkeeping
I am a new owner and want to inform current clients I want the announcement to be subtle. something like "same friendly faces, brand new name" the name is going from "Wendell R. Pickett, CPA, PC" to "Pickett Marlowe & Associates, LLC" I would like to emphasize a little on the Marlowe part of the name. I would like the words "Tax Accountants" below the name.
Accounting

```html
<!DOCTYPE html>
<html lang="en">
<head>
<meta charset="utf-8">
<title>Pickett Marlowe &amp; Associates – Name Change Postcard</title>
<link rel="stylesheet" href="https://fonts.googleapis.com/css2?family=Parisienne&family=Josefin+Sans:wght@300;400&family=Open+Sans:wght@400;600&family=PT+Sans+Narrow:wght@700&display=swap">
<style>
  :root {
    --backdrop: #efe9df;
    --gold-light: #d9b774;
    --gold-dark: #6b4a22;
    --burgundy: #5e110d;
    --burgundy-text: #7a1410;
    --cream: #f3e3c0;
    --peach: #f0cf94;
    --tan-panel: #ebd49c;
    --ink: #2a1a10;
    --white: #ffffff;
    --rule: #d9d3c7;
    --mark-blue: #2a4fa8;
  }
  * { box-sizing: border-box; margin: 0; padding: 0; }
  html, body { width: 1200px; height: 500px; overflow: hidden; }
  body { background: var(--backdrop); position: relative; font-family: "Open Sans", sans-serif; }

  /* Front side */
  .card-front {
    position: absolute; left: 25px; top: 12px; width: 575px; height: 448px;
    background: radial-gradient(ellipse at 40% 45%, var(--gold-light), #a47a3c 55%, var(--gold-dark));
    box-shadow: 0 2px 6px rgba(0,0,0,.25);
  }
  .announcement {
    position: absolute; left: 40px; top: 48px; width: 480px; height: 365px;
    background: var(--burgundy); border: 1px solid #a0783e;
    color: var(--cream); text-align: center;
  }
  .tagline {
    position: absolute; left: 0; right: 0; top: 40px;
    font-family: "Parisienne", cursive; font-size: 25px; line-height: 34px; color: #f1e6d4;
  }
  .front-mark {
    position: absolute; right: 30px; top: 52px; display: flex; align-items: center; gap: 5px;
    font-family: "Josefin Sans", sans-serif; font-size: 12px; color: var(--mark-blue); background: #f2ece0; padding: 3px 5px;
  }
  .front-mark .dot { width: 8px; height: 8px; background: var(--mark-blue); }
  .intro { position: absolute; left: 0; right: 0; top: 127px; font-weight: 600; font-size: 14.5px; line-height: 22px; color: #e9d8bd; }
  .old-name { position: absolute; left: 0; right: 0; top: 177px; font-family: "Josefin Sans", sans-serif; font-size: 19px; letter-spacing: .5px; color: #f1e2cc; }
  .to { position: absolute; left: 0; right: 0; top: 211px; font-size: 14px; color: #e9d8bd; }
  .new-name { position: absolute; left: 0; right: 0; top: 233px; font-family: "Josefin Sans", sans-serif; font-size: 19px; letter-spacing: .5px; color: var(--peach); }
  .new-name-role { position: absolute; left: 0; right: 0; top: 252px; font-family: "Josefin Sans", sans-serif; font-size: 15px; color: var(--peach); }
  .continuity { position: absolute; left: 0; right: 0; top: 292px; font-size: 11.5px; line-height: 15px; color: #d9c6ab; }
  .services-rule { position: absolute; left: 12px; right: 12px; top: 333px; border-top: 1px solid #a0783e; }
  .services { position: absolute; left: 0; right: 0; top: 341px; font-size: 17px; color: #fbf4e8; }

  /* Back side */
  .card-back {
    position: absolute; left: 618px; top: 12px; width: 557px; height: 448px;
    background: var(--white); box-shadow: 0 2px 6px rgba(0,0,0,.2);
  }
  .info-panel {
    position: absolute; left: 0; top: 0; width: 282px; height: 371px;
    background: var(--tan-panel); text-align: center; color: var(--ink);
  }
  .firm-name { position: absolute; left: 0; right: 0; top: 30px; font-family: "Josefin Sans", sans-serif; font-size: 19px; line-height: 23px; color: var(--burgundy-text); }
  .firm-role { position: absolute; left: 0; right: 0; top: 81px; font-family: "PT Sans Narrow", sans-serif; font-size: 12px; color: var(--burgundy-text); }
  .about { position: absolute; left: 10px; right: 10px; top: 110px; font-family: "PT Sans Narrow", sans-serif; font-size: 14px; line-height: 17.5px; }
  .about .highlight { color: var(--burgundy-text); font-size: 15px; }
  .phone { position: absolute; left: 0; right: 0; top: 316px; font-family: "PT Sans Narrow", sans-serif; font-size: 20px; color: var(--burgundy-text); display: flex; justify-content: center; align-items: center; gap: 3px; }
  .email { position: absolute; left: 0; right: 0; top: 338px; font-size: 13.5px; }

  .return-address { position: absolute; left: 318px; top: 58px; font-family: "Josefin Sans", sans-serif; }
  .back-mark { display: flex; align-items: center; gap: 4px; font-size: 11px; color: var(--mark-blue); margin-bottom: 8px; }
  .back-mark .dot { width: 7px; height: 7px; background: var(--mark-blue); }
  .return-name { font-size: 12.5px; line-height: 13px; color: var(--burgundy-text); }
  .return-role { font-family: "PT Sans Narrow", sans-serif; font-size: 8px; color: var(--burgundy-text); margin: 2px 0 6px 18px; }
  .return-street { font-family: "Open Sans", sans-serif; font-size: 12.5px; line-height: 17px; color: #222; padding-left: 4px; }
  .stamp-box { position: absolute; left: 432px; top: 53px; width: 88px; height: 88px; border: 1px solid #bdbdbd; }
  .address-line { position: absolute; left: 318px; width: 200px; border-top: 1px solid var(--rule); }
</style>
</head>
<body>

<section class="card-front">
  <div class="card-front-art" role="img" aria-label="Gold carved ornamental scrollwork background" style="position:absolute;inset:0;"></div>
  <div class="announcement">
    <p class="tagline">Same friendly faces,<br>brand new name</p>
    <div class="front-mark"><span class="dot"></span>Pickett Marlowe</div>
    <p class="intro">We are proud to announce that we are<br>changing company name from</p>
    <p class="old-name">Wendell R. Pickett, CPA, PC</p>
    <p class="to">to</p>
    <p class="new-name">Pickett MARLOWE &amp; Associates, LLC</p>
    <p class="new-name-role" style="top:257px">Tax Accountants</p>
    <p class="continuity">The company will continue to operate in its current<br>structure and your contacts will remain unchanged.</p>
    <div class="services-rule"></div>
    <p class="services">Payroll Processing | Business Consulting | Bookkeeping</p>
  </div>
</section>

<section class="card-back">
  <div class="info-panel">
    <p class="firm-name">Pickett MARLOWE<br>&amp; Associates, LLC</p>
    <p class="firm-role">Tax Accountants</p>
    <p class="about">We assist taxpayers and small businesses with taxes in Eagle, Colorado and the surrounding communities. Whether you are an individual or local business in or around Eagle, Colorado,<br><span class="highlight">Pickett MARLOWE &amp; Associates ,</span><br>has years of valuable experience as an IRS registered tax preparer.</p>
    <p class="phone">
      <svg width="14" height="16" viewBox="0 0 14 16" aria-hidden="true"><path d="M4 1 C1 3 1 13 4 15 L6 12 C4.5 10 4.5 6 6 4 Z" fill="none" stroke="#7a1410" stroke-width="1.6"/></svg>
      970.555.0142
    </p>
    <p class="email">info@pickettcpa.com</p>
  </div>

  <div class="return-address">
    <div class="back-mark"><span class="dot"></span>Pickett Marlowe</div>
    <p class="return-name">Pickett MARLOWE<br>&amp; Associates, LLC</p>
    <p class="return-role">Tax Accountants</p>
    <p class="return-street">482 Ridge St<br>Eagle, CO 81631</p>
  </div>
  <div class="stamp-box"></div>
  <div class="address-line" style="top:217px"></div>
  <div class="address-line" style="top:245px"></div>
  <div class="address-line" style="top:273px"></div>
  <div class="address-line" style="top:300px"></div>
</section>

</body>
</html>
```